Harbor Scholar Frame

The primary goal would be to develop a new vision for the Harbor Scholar Powerpt. I am attaching an older version called HS, I would like it updated to include our colors and our models with new images that make the presentation more relevant. I am also attaching brochures around the new curriculum. The Links below will give examples to the digital lessons: https://210.quillmora.net/review/content/7c2d4a91-583b-4f7e-b2d6-a4e91c0f5b37/review and https://210.quillmora.net/review/content/9f41b6c3-27da-4e85-81c4-c6d204a8e719/review. the Harbor scholar PWRPT should include some of these images and the color palet from the company brochure which is attached.
Target Market(s)
Education
Look and feel

```html
<!DOCTYPE html>
<html lang="en">
<head>
<meta charset="utf-8">
<title>Harbor Scholar Frame – Presentation Overview</title>
<link href="https://fonts.googleapis.com/css2?family=Montserrat:wght@300;400;500;600;700;800&display=swap" rel="stylesheet">
<style>
:root{
  --canvas:#a7a7ac;
  --slide-dark:#222224;
  --slide-light:#3f3f42;
  --orange:#f07c2b;
  --orange-deep:#e4601d;
  --gold:#d8b33a;
  --white:#ffffff;
  --box-gray:#4a4a4d;
  --rule:#6a6a6e;
}
*{box-sizing:border-box;margin:0;padding:0}
html,body{width:1200px;height:2910px;overflow:hidden;background:var(--canvas);font-family:"Montserrat",sans-serif}
.deck{position:relative;width:1200px;height:2910px}
.slide{position:absolute;width:554px;height:312px;overflow:hidden;color:var(--white);
  background:linear-gradient(160deg,var(--slide-dark) 0%,#2b2b2d 50%,var(--slide-light) 100%)}
.brand{position:absolute;left:29px;top:40px;display:flex;align-items:center;gap:6px;font-weight:500;font-size:21px;letter-spacing:.2px;color:var(--white);z-index:2}
.brand::before{content:"";width:14px;height:14px;background:var(--orange)}
.pg{position:absolute;right:22px;bottom:16px;font-size:8px;font-weight:600;z-index:2}
.tag{position:absolute;right:38px;top:46px;background:var(--orange);font-size:10px;font-weight:700;padding:4px 12px;border-radius:2px}
.heading{position:absolute;left:30px;font-size:14px;font-weight:700;line-height:1.25;z-index:2}
.heading span{display:block;font-weight:300;font-size:14px}
.heading::after{content:"";display:block;width:20px;height:1px;background:var(--white);margin-top:12px}
.heading.plain::after{display:none}

/* photo fills – soft multi-tone gradients in the tones of each photo */
.ph-curriculum{background:
  radial-gradient(ellipse 60% 30% at 55% 72%,rgba(214,196,168,.85),rgba(214,196,168,0) 70%),
  radial-gradient(ellipse 70% 25% at 45% 88%,rgba(150,128,100,.9),rgba(150,128,100,0) 75%),
  radial-gradient(ellipse 80% 40% at 50% 25%,rgba(92,96,100,.9),rgba(92,96,100,0) 75%),
  linear-gradient(180deg,#2a2b2d 0%,#3e4043 45%,#4a4540 75%,#242426 100%)}
.ph-teacher{background:
  radial-gradient(ellipse 40% 22% at 50% 26%,rgba(214,170,140,.95),rgba(214,170,140,0) 75%),
  radial-gradient(ellipse 55% 45% at 50% 68%,rgba(170,196,214,.95),rgba(170,196,214,0) 75%),
  radial-gradient(ellipse 45% 60% at 85% 30%,rgba(60,92,76,.9),rgba(60,92,76,0) 75%),
  linear-gradient(180deg,#4d5e58 0%,#7c8c8a 40%,#8ea2b4 70%,#2f3236 100%)}
.ph-student{background:
  radial-gradient(ellipse 40% 22% at 55% 30%,rgba(236,196,168,.95),rgba(236,196,168,0) 75%),
  radial-gradient(ellipse 35% 25% at 50% 16%,rgba(196,150,96,.9),rgba(196,150,96,0) 75%),
  radial-gradient(ellipse 60% 35% at 50% 70%,rgba(210,92,130,.95),rgba(210,92,130,0) 75%),
  radial-gradient(ellipse 40% 40% at 12% 35%,rgba(150,170,190,.8),rgba(150,170,190,0) 75%),
  linear-gradient(180deg,#8e9aa0 0%,#b7a9a2 40%,#a8556e 72%,#333133 100%)}
.ph-tech{background:
  radial-gradient(ellipse 45% 35% at 45% 38%,rgba(255,255,255,.95),rgba(255,255,255,0) 75%),
  radial-gradient(ellipse 25% 6% at 40% 16%,rgba(232,110,60,.9),rgba(232,110,60,0) 80%),
  radial-gradient(ellipse 30% 20% at 60% 45%,rgba(150,190,215,.7),rgba(150,190,215,0) 75%),
  radial-gradient(ellipse 20% 50% at 92% 35%,rgba(40,40,44,.8),rgba(40,40,44,0) 75%),
  linear-gradient(180deg,#cfd3d6 0%,#eeeeee 40%,#8f9397 70%,#2b2b2d 100%)}

/* tiles */
.tiles{position:absolute;left:36px;top:94px;display:flex;gap:14px}
.tile{position:relative;width:109px;height:165px;border-radius:3px;overflow:hidden}
.tile .ph{position:absolute;inset:0}
.tile .ph::before{content:"";position:absolute;left:0;right:0;bottom:0;height:45%;background:linear-gradient(180deg,rgba(30,30,32,0),rgba(30,30,32,.75))}
.tile.dim .ph::after{content:"";position:absolute;inset:0;background:rgba(44,44,46,.55)}
.tile.active .ph::after{content:"";position:absolute;inset:0;background:linear-gradient(180deg,rgba(240,124,43,.05) 0%,rgba(240,124,43,.6) 55%,rgba(240,124,43,.95) 100%)}
.tile.active .ph::before{display:none}
.tile-label{position:absolute;left:0;right:0;bottom:12px;text-align:center;font-size:11.5px;font-weight:700;letter-spacing:.2px;z-index:1}
.tile.framed{outline:2px solid var(--orange);outline-offset:4px}
.caption{position:absolute;left:36px;width:478px;top:276px;text-align:center;font-size:11.5px;font-weight:700}

/* slide 1 */
.cover{background:var(--white)}
.cover svg.bg{position:absolute;inset:0}
.cover .mock{position:absolute;left:262px;top:56px;width:262px;height:176px;border-radius:5px;
  background:
   radial-gradient(ellipse 30% 25% at 78% 70%,rgba(120,150,180,.55),rgba(120,150,180,0) 75%),
   linear-gradient(90deg,rgba(232,110,60,.85) 0 38%,rgba(0,0,0,0) 38%) 45% 16% / 40% 5% no-repeat,
   radial-gradient(ellipse 55% 45% at 40% 40%,#fbfbfb,#e8e9eb 70%),
   linear-gradient(180deg,#f2f2f2,#c9ccd0);
  box-shadow:0 0 0 6px #1c1c1e inset,0 10px 18px rgba(0,0,0,.35)}
.cover-title{position:absolute;left:30px;top:234px;font-size:13.5px;font-weight:700;letter-spacing:.3px}
.cover-btn{position:absolute;left:30px;top:254px;border:1.5px solid var(--orange);border-radius:2px;font-size:9px;font-weight:600;padding:4px 16px;letter-spacing:.3px}

/* slide 2 */
.evo{position:absolute;left:220px;top:73px;display:grid;grid-template-columns:repeat(3,90px);gap:15px;row-gap:14px}
.evo-tile{position:relative;width:90px;height:90px;border-radius:2px;overflow:hidden;text-align:center}
.evo-tile .ph{position:absolute;inset:0}
.evo-tile .ph::after{content:"";position:absolute;inset:0;background:linear-gradient(180deg,rgba(25,25,27,.15),rgba(25,25,27,.55))}
.ph-lab{background:radial-gradient(ellipse 60% 30% at 50% 30%,#6fa6d8,rgba(111,166,216,0) 75%),radial-gradient(ellipse 70% 30% at 50% 70%,#3b4f66,rgba(59,79,102,0) 75%),linear-gradient(180deg,#4f6f90,#26303b)}
.ph-board{background:radial-gradient(ellipse 40% 50% at 35% 40%,#e6ecea,rgba(230,236,234,0) 75%),radial-gradient(ellipse 25% 45% at 80% 45%,#b77f5e,rgba(183,127,94,0) 75%),linear-gradient(180deg,#bfcac6,#7e7a70)}
.ph-incls{background:radial-gradient(ellipse 40% 40% at 40% 35%,#e2c6b2,rgba(226,198,178,0) 75%),radial-gradient(ellipse 40% 40% at 75% 65%,#c9a486,rgba(201,164,134,0) 75%),linear-gradient(180deg,#c9c1b8,#6e6257)}
.ph-print{background:radial-gradient(ellipse 45% 35% at 30% 30%,#e8eef4,rgba(232,238,244,0) 75%),radial-gradient(ellipse 50% 35% at 70% 60%,#8fae6a,rgba(143,174,106,0) 75%),linear-gradient(180deg,#9fb4c8,#3f4a52)}
.ph-dtp{background:radial-gradient(ellipse 45% 45% at 45% 40%,#dfe6da,rgba(223,230,218,0) 75%),radial-gradient(ellipse 30% 30% at 25% 70%,#78a25a,rgba(120,162,90,0) 75%),linear-gradient(180deg,#c8cec2,#5f5c55)}
.evo-tile.accent .ph{background:radial-gradient(ellipse 55% 35% at 45% 30%,#f6ece6,rgba(246,236,230,0) 75%),linear-gradient(180deg,#e6d6cc 0%,#f0894a 55%,var(--orange) 100%)}
.evo-tile.accent .ph::after{display:none}
.evo-name{position:absolute;left:0;right:0;top:46px;font-size:8px;line-height:1.1}
.evo-name.two{top:40px}
.evo-year{position:absolute;left:50%;transform:translateX(-50%);top:66px;background:var(--orange);font-size:8px;font-weight:700;padding:2px 8px;white-space:nowrap}

/* slide 3 */
.intro{position:absolute;left:40px;top:92px;width:284px;font-size:5.6px;line-height:1.35;color:var(--white)}
.intro p{margin-bottom:6px}
.book{position:absolute;left:346px;top:55px;width:138px;height:215px;border-radius:2px;
  background:
   radial-gradient(ellipse 60% 30% at 50% 30%,rgba(255,255,255,.22),rgba(255,255,255,0) 75%),
   radial-gradient(ellipse 60% 18% at 50% 72%,rgba(255,255,255,.14),rgba(255,255,255,0) 75%),
   linear-gradient(90deg,#0f2a55 0 6%,#1c4a91 6% 8%,#2c63b8 30%,#2a5cab 70%,#1b3f7a 100%);
  box-shadow:6px 6px 14px rgba(0,0,0,.5)}

/* diagrams */
.node{position:absolute;display:flex;align-items:center;justify-content:center;text-align:center;font-size:7.5px;font-weight:600;line-height:1.1;border-radius:2px;z-index:2}
.node.orange{background:var(--orange)}
.node.gray{background:var(--box-gray)}
.node.gold{background:var(--gold)}
svg.wires{position:absolute;inset:0;z-index:1}

/* slide 5 */
.lms-intro{position:absolute;left:40px;top:152px;font-size:8px}
.lms-list{position:absolute;left:40px;top:182px;font-size:8.2px;list-style:none;line-height:1.9}
.lms-list li::before{content:"";display:inline-block;width:4px;height:4px;border-radius:50%;background:var(--orange);margin-right:8px;vertical-align:middle}
.hero{position:absolute;left:280px;top:0;width:274px;height:312px;background:
  radial-gradient(ellipse 28% 22% at 55% 30%,rgba(92,58,40,.95),rgba(92,58,40,0) 75%),
  radial-gradient(ellipse 30% 14% at 55% 14%,rgba(210,210,214,.85),rgba(210,210,214,0) 75%),
  radial-gradient(ellipse 45% 25% at 30% 62%,rgba(120,120,126,.85),rgba(120,120,126,0) 75%),
  radial-gradient(ellipse 50% 30% at 70% 85%,rgba(248,214,176,.9),rgba(248,214,176,0) 75%),
  radial-gradient(ellipse 20% 40% at 95% 10%,rgba(70,56,44,.9),rgba(70,56,44,0) 75%),
  linear-gradient(160deg,#7a5a3c,#c88a4e 45%,#eab27a 75%,#c98a56)}

/* slide 11 */
.backdrop{position:absolute;left:230px;top:0;width:324px;height:312px;background:
  radial-gradient(ellipse 22% 20% at 55% 32%,rgba(196,160,138,.45),rgba(196,160,138,0) 75%),
  radial-gradient(ellipse 26% 18% at 55% 18%,rgba(210,190,150,.35),rgba(210,190,150,0) 75%),
  radial-gradient(ellipse 45% 40% at 55% 75%,rgba(70,70,74,.6),rgba(70,70,74,0) 75%)}

/* slide 12 */
.feature-grid{position:absolute;left:89px;top:81px;display:grid;grid-template-columns:repeat(4,88px);grid-auto-rows:88px;gap:3px}
.feature{background:#58585b;display:flex;flex-direction:column;align-items:center;padding-top:16px;text-align:center;font-size:7px;font-weight:600;line-height:1.15;padding-left:4px;padding-right:4px}
.feature svg{width:22px;height:22px;margin-bottom:9px;flex:none}
.feature small{display:block;font-weight:400;font-size:5.5px;margin-top:1px}
.feature.photo{padding:0;background:
  radial-gradient(ellipse 30% 25% at 50% 38%,rgba(240,206,180,.95),rgba(240,206,180,0) 75%),
  radial-gradient(ellipse 40% 30% at 50% 25%,rgba(190,140,90,.8),rgba(190,140,90,0) 75%),
  linear-gradient(180deg,#d9c2ad,#e88a4a 60%,var(--orange))}

/* slide 16 */
.scan-title{position:absolute;right:26px;top:45px;font-size:12px;font-weight:700}
.scan{position:absolute;left:30px;top:70px;width:500px;border-collapse:collapse;font-size:6.8px}
.scan th{font-weight:500;height:30px;vertical-align:middle;text-align:center;line-height:1.1}
.scan th:first-child{color:var(--orange);text-align:left;padding-left:18px}
.scan td{height:20.4px;text-align:center;border-top:1px solid var(--rule)}
.scan td:first-child{text-align:left;padding-left:20px}
.scan .hs{background:var(--orange)}
.scan svg{width:12px;height:10px}
</style>
</head>
<body>
<svg width="0" height="0" style="position:absolute">
  <defs>
    <symbol id="tick" viewBox="0 0 12 10"><polyline points="1,5 4.5,8.5 11,1" fill="none" stroke="#fff" stroke-width="1.2"/></symbol>
    <marker id="arr" viewBox="0 0 8 8" refX="6" refY="4" markerWidth="6" markerHeight="6" orient="auto-start-reverse"><path d="M0,0 L8,4 L0,8" fill="none" stroke="#fff" stroke-width="1.3"/></marker>
    <marker id="arr-o" viewBox="0 0 8 8" refX="6" refY="4" markerWidth="6" markerHeight="6" orient="auto"><path d="M0,0 L8,4 L0,8" fill="none" stroke="#f07c2b" stroke-width="1.3"/></marker>
  </defs>
</svg>

<main class="deck">

  <!-- 1 cover -->
  <section class="slide cover" style="left:34px;top:50px">
    <svg class="bg" viewBox="0 0 554 312" preserveAspectRatio="none">
      <polygon points="225,0 554,0 554,40 0,232 0,205" fill="#f07c2b"/>
      <polygon points="0,232 554,40 554,312 0,312" fill="#2b2b2d"/>
      <polygon points="554,150 554,312 420,312" fill="#ffffff"/>
    </svg>
    <div class="mock" role="img" aria-label="Laptop, desktop and phone showing a digital lesson"></div>
    <div class="brand" style="top:36px;color:#2b2b2d">Tidemark</div>
    <h1 class="cover-title">HARBOR SCHOLAR PLATFORM</h1>
    <div class="cover-btn">LEARN MORE</div>
  </section>

  <!-- 2 evolution -->
  <section class="slide" style="left:615px;top:50px">
    <div class="brand">Tidemark</div>
    <h2 class="heading" style="top:130px">Evolution of Digital<span>Instructional Tools</span></h2>
    <div class="evo">
      <div class="evo-tile"><div class="ph ph-lab" role="img" aria-label="Computer lab photo"></div><div class="evo-name">Computer Labs</div><div class="evo-year">1985</div></div>
      <div class="evo-tile"><div class="ph ph-board" role="img" aria-label="Teacher at an electronic whiteboard"></div><div class="evo-name two">Electronic<br>Whiteboards</div><div class="evo-year">2000</div></div>
      <div class="evo-tile"><div class="ph ph-incls" role="img" aria-label="Students computing in class"></div><div class="evo-name two">In-class<br>Computing</div><div class="evo-year">2010</div></div>
      <div class="evo-tile"><div class="ph ph-print" role="img" aria-label="Printed page becoming a digital screen"></div><div class="evo-name">Print → Digital</div><div class="evo-year">2012</div></div>
      <div class="evo-tile"><div class="ph ph-dtp" role="img" aria-label="Classroom using a teaching platform"></div><div class="evo-name two">Harbor Scholar<br>Platforms</div><div class="evo-year">Next Gen</div></div>
      <div class="evo-tile accent"><div class="ph" role="img" aria-label="Screen of the teaching platform"></div></div>
    </div>
    <div class="pg">2</div>
  </section>

  <!-- 3 intro -->
  <section class="slide" style="left:34px;top:395px">
    <div class="brand">Tidemark</div>
    <div class="intro">
      <p>The Harbor Scholar Platform contains a comprehensive curriculum of guided learning sequences that include applet activities, multimedia presentations, practice exercises, and activities. Before class the teacher uses <b>planning tools</b> to prepare; during class he uses multimedia to introduce a topic, an math tool to explore a mathematics concept, and practice exercises. After class, the teacher can review each student's progress, trends in the class performance, and begin the process for planning tomorrow's lessons.</p>
      <p>The platform provides <b>powerful tools</b> to the teacher for planning and managing lessons, customizing instruction to individuals, and providing quick feedback on all activities. It facilitates the management of groups of students without losing focus on individuals. It frees up the teacher for small group work and individual tutoring. In these ways, the platform respects the role of schools in today's society by teaching to standards and preparing students for high-stakes tests.</p>
      <p>At the same time, the Harbor Scholar Platform deploys a social constructivist pedagogy and provides tools and content to build on that approach. It features open-ended explorations, student collaboration, shared work, and group discussion. In this way the platform goes beyond the standards and engages students in their learning, preparing them in a deep way for their place in a technology-rich society.</p>
    </div>
    <div class="book" role="img" aria-label="Cover of the book Harbor Scholar Platforms"></div>
    <div class="pg">3</div>
  </section>

  <!-- 4 traditional loop -->
  <section class="slide" style="left:615px;top:395px">
    <div class="brand">Tidemark</div>
    <h2 class="heading" style="top:96px">Traditional LMS<span>Instructional Loop</span></h2>
    <svg class="wires" viewBox="0 0 554 312">
      <path d="M72,182 Q130,125 188,182" fill="none" stroke="#f07c2b" stroke-width="1.5" marker-end="url(#arr-o)"/>
      <path d="M188,228 Q130,285 72,228" fill="none" stroke="#f07c2b" stroke-width="1.5" marker-end="url(#arr-o)"/>
      <line x1="202" y1="206" x2="234" y2="206" stroke="#fff" stroke-width="1.2" marker-end="url(#arr)"/>
      <line x1="301" y1="206" x2="331" y2="206" stroke="#fff" stroke-width="1.2" marker-start="url(#arr)" marker-end="url(#arr)"/>
    </svg>
    <div class="node orange" style="left:34px;top:189px;width:64px;height:35px">Content<br>Management</div>
    <div class="node orange" style="left:136px;top:189px;width:64px;height:35px">Assessment</div>
    <div class="node gray" style="left:240px;top:189px;width:58px;height:35px">Grade<br>Book</div>
    <div class="node gray" style="left:337px;top:189px;width:62px;height:35px">SIS</div>
    <div class="pg">4</div>
  </section>

  <!-- 5 traditional lms -->
  <section class="slide" style="left:34px;top:740px">
    <div class="brand">Tidemark</div>
    <h2 class="heading plain" style="left:40px;top:105px">Traditional LMS</h2>
    <div style="position:absolute;left:40px;top:133px;width:20px;height:1px;background:#fff"></div>
    <p class="lms-intro">Skinnerian Teaching Machines—ILS's</p>
    <ul class="lms-list">
      <li>"Teacher Proof" Technology</li>
      <li>Closed Curriculum</li>
      <li>Fixed Map from Assessment to Curriculum</li>
      <li>Lab or Back of the Room</li>
      <li>One student only</li>
    </ul>
    <div class="hero" role="img" aria-label="Student with headphones working at a laptop"></div>
    <div class="pg">5</div>
  </section>

  <!-- 6 locus -->
  <section class="slide" style="left:615px;top:740px">
    <div class="brand">Tidemark</div>
    <div class="tag">Traditional LMS</div>
    <div class="tiles">
      <div class="tile"><div class="ph ph-curriculum" role="img" aria-label="Stack of textbooks and calculator"></div><div class="tile-label">Curriculum</div></div>
      <div class="tile"><div class="ph ph-teacher" role="img" aria-label="Teacher holding a tablet"></div><div class="tile-label">Teacher</div></div>
      <div class="tile"><div class="ph ph-student" role="img" aria-label="Student working on a laptop"></div><div class="tile-label">Student</div></div>
      <div class="tile"><div class="ph ph-tech" role="img" aria-label="Computer showing lesson software"></div><div class="tile-label">Technology</div></div>
    </div>
    <p class="caption">Where is the Locus of Control?</p>
    <div class="pg">6</div>
  </section>

  <!-- 7 teacher-centered -->
  <section class="slide" style="left:34px;top:1083px">
    <div class="brand">Tidemark</div>
    <div class="tag">Traditional LMS</div>
    <div class="tiles">
      <div class="tile dim"><div class="ph ph-curriculum" role="img" aria-label="Stack of textbooks and calculator"></div><div class="tile-label">Curriculum</div></div>
      <div class="tile active"><div class="ph ph-teacher" role="img" aria-label="Teacher holding a tablet"></div><div class="tile-label">Teacher</div></div>
      <div class="tile dim"><div class="ph ph-student" role="img" aria-label="Student working on a laptop"></div><div class="tile-label">Student</div></div>
      <div class="tile dim"><div class="ph ph-tech" role="img" aria-label="Computer showing lesson software"></div><div class="tile-label">Technology</div></div>
    </div>
    <p class="caption">Teacher-Centered</p>
    <div class="pg">7</div>
  </section>

  <!-- 8 curriculum-centered -->
  <section class="slide" style="left:615px;top:1083px">
    <div class="brand">Tidemark</div>
    <div class="tag">Traditional LMS</div>
    <div class="tiles">
      <div class="tile active"><div class="ph ph-curriculum" role="img" aria-label="Stack of textbooks and calculator"></div><div class="tile-label">Curriculum</div></div>
      <div class="tile dim"><div class="ph ph-teacher" role="img" aria-label="Teacher holding a tablet"></div><div class="tile-label">Teacher</div></div>
      <div class="tile dim"><div class="ph ph-student" role="img" aria-label="Student working on a laptop"></div><div class="tile-label">Student</div></div>
      <div class="tile dim"><div class="ph ph-tech" role="img" aria-label="Computer showing lesson software"></div><div class="tile-label">Technology</div></div>
    </div>
    <p class="caption">Curriculum-Centered</p>
    <div class="pg">8</div>
  </section>

  <!-- 9 student-centered -->
  <section class="slide" style="left:34px;top:1427px">
    <div class="brand">Tidemark</div>
    <div class="tag">Traditional LMS</div>
    <div class="tiles">
      <div class="tile dim"><div class="ph ph-curriculum" role="img" aria-label="Stack of textbooks and calculator"></div><div class="tile-label">Curriculum</div></div>
      <div class="tile dim"><div class="ph ph-teacher" role="img" aria-label="Teacher holding a tablet"></div><div class="tile-label">Teacher</div></div>
      <div class="tile active"><div class="ph ph-student" role="img" aria-label="Student working on a laptop"></div><div class="tile-label">Student</div></div>
      <div class="tile dim"><div class="ph ph-tech" role="img" aria-label="Computer showing lesson software"></div><div class="tile-label">Technology</div></div>
    </div>
    <p class="caption">Student-Centered</p>
    <div class="pg">9</div>
  </section>

  <!-- 10 technology-centered -->
  <section class="slide" style="left:615px;top:1427px">
    <div class="brand">Tidemark</div>
    <div class="tag">Traditional LMS</div>
    <div class="tiles">
      <div class="tile dim"><div class="ph ph-curriculum" role="img" aria-label="Stack of textbooks and calculator"></div><div class="tile-label">Curriculum</div></div>
      <div class="tile dim"><div class="ph ph-teacher" role="img" aria-label="Teacher holding a tablet"></div><div class="tile-label">Teacher</div></div>
      <div class="tile dim"><div class="ph ph-student" role="img" aria-label="Student working on a laptop"></div><div class="tile-label">Student</div></div>
      <div class="tile active framed"><div class="ph ph-tech" role="img" aria-label="Computer showing lesson software"></div><div class="tile-label">Technology</div></div>
    </div>
    <p class="caption">Technology-Centered</p>
    <div class="pg">10</div>
  </section>

  <!-- 11 platform loops -->
  <section class="slide" style="left:34px;top:1771px">
    <div class="backdrop" role="img" aria-label="Smiling teacher in soft focus"></div>
    <div class="brand" style="top:32px">Tidemark</div>
    <h2 class="heading plain" style="left:30px;top:70px">Harbor Scholar Platform<span>Instructional Loops</span></h2>
    <svg class="wires" viewBox="0 0 554 312">
      <polyline points="216,135 93,135 93,196" fill="none" stroke="#fff" stroke-width="1.2" marker-end="url(#arr)"/>
      <line x1="126" y1="218" x2="160" y2="218" stroke="#fff" stroke-width="1.2" marker-end="url(#arr)"/>
      <line x1="328" y1="218" x2="361" y2="218" stroke="#fff" stroke-width="1.2" marker-end="url(#arr)"/>
      <line x1="429" y1="218" x2="462" y2="218" stroke="#fff" stroke-width="1.2" marker-start="url(#arr)" marker-end="url(#arr)"/>
      <path d="M170,198 A78,78 0 0 1 208,142" fill="none" stroke="#d8b33a" stroke-width="1.5" marker-end="url(#arr-o)"/>
      <path d="M280,138 A78,78 0 0 1 320,198" fill="none" stroke="#d8b33a" stroke-width="1.5" marker-end="url(#arr-o)"/>
      <path d="M202,200 Q245,150 282,196" fill="none" stroke="#f07c2b" stroke-width="1.5" marker-end="url(#arr-o)"/>
      <path d="M282,240 Q245,290 202,240" fill="none" stroke="#f07c2b" stroke-width="1.5" marker-end="url(#arr-o)"/>
      <path d="M320,240 A90,90 0 0 1 170,240" fill="none" stroke="#d8b33a" stroke-width="1.5" marker-end="url(#arr-o)"/>
    </svg>
    <div class="node gold" style="left:216px;top:123px;width:62px;height:24px">Teacher</div>
    <div class="node gray" style="left:62px;top:201px;width:62px;height:33px">Course<br>Syllabus</div>
    <div class="node orange" style="left:164px;top:201px;width:62px;height:33px">Content<br>Management</div>
    <div class="node orange" style="left:264px;top:201px;width:62px;height:33px">Assessment</div>
    <div class="node gray" style="left:365px;top:201px;width:62px;height:33px">Grade<br>Book</div>
    <div class="node gray" style="left:466px;top:201px;width:62px;height:33px">SIS</div>
    <div class="pg">11</div>
  </section>

  <!-- 12 features -->
  <section class="slide" style="left:615px;top:1771px">
    <div class="brand" style="top:32px">Tidemark</div>
    <div class="feature-grid">
      <div class="feature"><svg viewBox="0 0 24 24" fill="none" stroke="#fff" stroke-width="1.2"><rect x="4" y="4" width="16" height="13"/><circle cx="12" cy="10" r="2.5"/><path d="M8 17 q4-5 8 0"/></svg>Designed for Classroom Use<small>Real Time Classroom Management</small></div>
      <div class="feature"><svg viewBox="0 0 24 24" fill="none" stroke="#fff" stroke-width="1.2"><circle cx="12" cy="8" r="4"/><path d="M4 21 q8-10 16 0"/></svg>Teacher-Centric<small>Scaffolds Teachers</small></div>
      <div class="feature"><svg viewBox="0 0 24 24" fill="none" stroke="#fff" stroke-width="1.2"><path d="M5 19 L7 13 L17 3 L21 7 L11 17 Z"/><line x1="4" y1="21" x2="20" y2="21"/></svg>Open Curriculum Flexible, Teacher-Modifiable</div>
      <div class="feature"><svg viewBox="0 0 24 24" fill="none" stroke="#fff" stroke-width="1.2"><circle cx="12" cy="12" r="3.5"/><circle cx="12" cy="12" r="8" stroke-dasharray="3 2"/></svg>Lesson Planning Tools</div>
      <div class="feature"><svg viewBox="0 0 24 24" fill="none" stroke="#fff" stroke-width="1.2"><circle cx="9" cy="8" r="4"/><path d="M2 20 q7-9 14 0"/><path d="M18 6 v6 M15 9 h6"/></svg>Individual, Group, and Whole Class Curricula</div>
      <div class="feature"><svg viewBox="0 0 24 24" fill="none" stroke="#fff" stroke-width="1.2"><circle cx="5" cy="17" r="2"/><circle cx="12" cy="8" r="2"/><circle cx="19" cy="17" r="2"/><path d="M6.5 15.5 L10.5 9.5 M13.5 9.5 L17.5 15.5"/></svg>Collaborative, Project Centered</div>
      <div class="feature"><svg viewBox="0 0 24 24" fill="none" stroke="#fff" stroke-width="1.2"><path d="M4 10 v10 h16 v-10"/><path d="M8 10 h-4 M20 10 h-8 v-4 l-3 3"/></svg>Adaptive Assessment Loop for Personalized Instruction</div>
      <div class="feature photo" role="img" aria-label="Student giving a thumbs up in class"></div>
    </div>
    <div class="pg">12</div>
  </section>

  <!-- 13 hs locus -->
  <section class="slide" style="left:34px;top:2115px">
    <div class="brand">Tidemark</div>
    <div class="tag">HS Platform</div>
    <div class="tiles">
      <div class="tile"><div class="ph ph-curriculum" role="img" aria-label="Stack of textbooks and calculator"></div><div class="tile-label">Curriculum</div></div>
      <div class="tile"><div class="ph ph-teacher" role="img" aria-label="Teacher holding a tablet"></div><div class="tile-label">Teacher</div></div>
      <div class="tile"><div class="ph ph-student" role="img" aria-label="Student working on a laptop"></div><div class="tile-label">Student</div></div>
      <div class="tile"><div class="ph ph-tech" role="img" aria-label="Computer showing lesson software"></div><div class="tile-label">Technology</div></div>
    </div>
    <p class="caption">Where is the Locus of Control?</p>
    <div class="pg">13</div>
  </section>

  <!-- 14 hs teacher -->
  <section class="slide" style="left:615px;top:2115px">
    <div class="brand">Tidemark</div>
    <div class="tag">HS Platform</div>
    <div class="tiles">
      <div class="tile dim"><div class="ph ph-curriculum" role="img" aria-label="Stack of textbooks and calculator"></div><div class="tile-label">Curriculum</div></div>
      <div class="tile active framed"><div class="ph ph-teacher" role="img" aria-label="Teacher holding a tablet"></div><div class="tile-label">Teacher</div></div>
      <div class="tile dim"><div class="ph ph-student" role="img" aria-label="Student working on a laptop"></div><div class="tile-label">Student</div></div>
      <div class="tile dim"><div class="ph ph-tech" role="img" aria-label="Computer showing lesson software"></div><div class="tile-label">Technology</div></div>
    </div>
    <p class="caption">Teacher-Centered</p>
    <div class="pg">14</div>
  </section>

  <!-- 15 hs student -->
  <section class="slide" style="left:34px;top:2460px">
    <div class="brand">Tidemark</div>
    <div class="tag">HS Platform</div>
    <div class="tiles">
      <div class="tile dim"><div class="ph ph-curriculum" role="img" aria-label="Stack of textbooks and calculator"></div><div class="tile-label">Curriculum</div></div>
      <div class="tile dim"><div class="ph ph-teacher" role="img" aria-label="Teacher holding a tablet"></div><div class="tile-label">Teacher</div></div>
      <div class="tile active framed"><div class="ph ph-student" role="img" aria-label="Student working on a laptop"></div><div class="tile-label">Student</div></div>
      <div class="tile dim"><div class="ph ph-tech" role="img" aria-label="Computer showing lesson software"></div><div class="tile-label">Technology</div></div>
    </div>
    <p class="caption">Student-Centered</p>
    <div class="pg">15</div>
  </section>

  <!-- 16 delivery scan -->
  <section class="slide" style="left:615px;top:2460px">
    <div class="brand" style="top:32px">Tidemark</div>
    <h2 class="scan-title">Instructional Delivery Scan</h2>
    <table class="scan">
      <thead>
        <tr><th>21st Century School Environment</th><th>Course<br>Platform LMS</th><th>Course<br>Delivery LMS</th><th class="hs">Harbor Scholar<br>Platform</th><th>Text book</th><th>E-book</th></tr>
      </thead>
      <tbody>
        <tr><td>Interactive Digital Environment</td><td><svg><use href="#tick"/></svg></td><td><svg><use href="#tick"/></svg></td><td class="hs"><svg><use href="#tick"/></svg></td><td></td><td></td></tr>
        <tr><td>Virtual Courses</td><td><svg><use href="#tick"/></svg></td><td><svg><use href="#tick"/></svg></td><td class="hs"></td><td></td><td></td></tr>
        <tr><td>Teacher Administration Tools</td><td><svg><use href="#tick"/></svg></td><td><svg><use href="#tick"/></svg></td><td class="hs"><svg><use href="#tick"/></svg></td><td><svg><use href="#tick"/></svg></td><td><svg><use href="#tick"/></svg></td></tr>
        <tr><td>Student Administration Tools</td><td><svg><use href="#tick"/></svg></td><td><svg><use href="#tick"/></svg></td><td class="hs"><svg><use href="#tick"/></svg></td><td><svg><use href="#tick"/></svg></td><td><svg><use href="#tick"/></svg></td></tr>
        <tr><td>Course Authoring Tools</td><td><svg><use href="#tick"/></svg></td><td></td><td class="hs"><svg><use href="#tick"/></svg></td><td></td><td></td></tr>
        <tr><td>Curriculum Content</td><td></td><td><svg><use href="#tick"/></svg></td><td class="hs"><svg><use href="#tick"/></svg></td><td><svg><use href="#tick"/></svg></td><td><svg><use href="#tick"/></svg></td></tr>
        <tr><td>Assessment Content</td><td></td><td><svg><use href="#tick"/></svg></td><td class="hs"><svg><use href="#tick"/></svg></td><td><svg><use href="#tick"/></svg></td><td><svg><use href="#tick"/></svg></td></tr>
        <tr><td>Classroom Support</td><td></td><td></td><td class="hs"><svg><use href="#tick"/></svg></td><td><svg><use href="#tick"/></svg></td><td></td></tr>
        <tr><td>Pedagogical Support</td><td></td><td></td><td class="hs"><svg><use href="#tick"/></svg></td><td><svg><use href="#tick"/></svg></td><td><svg><use href="#tick"/></svg></td></tr>
      </tbody>
    </table>
    <div class="pg">16</div>
  </section>

</main>
</body>
</html>
```